Nurturing Victors 6x9 book soft cover- front cover only

We need a book cover for a softcover book. We will need final files in Photoshop or InDesign is preferred.

Overall Title:
Nurturing Victors
Subtitle:
The Foundations of Humble Mentoring for Trainers, Instructors and Players
Author:
by Dr. Martin Hollis

The audience is high school and college coaches however we don't want the standard picture with words over the top. Make it a creative design but keep it mind it's a little academic.

```html
<!DOCTYPE html>
<html lang="en">
<head>
<meta charset="utf-8">
<title>Nurturing Victors — Front Cover</title>
<link href="https://fonts.googleapis.com/css2?family=Jost:wght@400;600&family=Roboto:wght@500&family=Bebas+Neue&display=swap" rel="stylesheet">
<style>
  :root {
    --backdrop: #c3bdad;
    --sky-top: #2a2638;
    --sky-upper: #4a3a44;
    --sky-mid: #7a5f4c;
    --sky-glow: #e2bd72;
    --sun-core: #f6dc98;
    --ground: #241f2c;
    --title-ink: #c8ccd4;
    --subtitle-ink: #c4c4c8;
    --author-ink: #d0d1d6;
  }
  html, body {
    margin: 0;
    padding: 0;
    width: 1200px;
    height: 924px;
    overflow: hidden;
    background: var(--backdrop);
  }
  .canvas {
    position: relative;
    width: 1200px;
    height: 924px;
  }
  .cover {
    position: absolute;
    left: 340px;
    top: 132px;
    width: 444px;
    height: 644px;
    overflow: hidden;
  }
  .cover-art {
    position: absolute;
    inset: 0;
    width: 100%;
    height: 100%;
  }
  .title {
    position: absolute;
    top: 96px;
    left: 0;
    right: 0;
    margin: 0;
    text-align: center;
    color: var(--title-ink);
    font-family: "Jost", sans-serif;
    line-height: 1;
  }
  .title-light {
    display: block;
    font-weight: 400;
    font-size: 47px;
    letter-spacing: 2px;
  }
  .title-bold {
    display: block;
    font-weight: 600;
    font-size: 54px;
    letter-spacing: 1px;
    margin-top: -3px;
  }
  .subtitle {
    position: absolute;
    top: 196px;
    left: 50px;
    right: 50px;
    margin: 0;
    text-align: center;
    color: var(--subtitle-ink);
    font-family: "Roboto", sans-serif;
    font-weight: 500;
    font-size: 10.5px;
    line-height: 12px;
    text-transform: uppercase;
  }
  .author {
    position: absolute;
    top: 602px;
    left: 0;
    right: 0;
    margin: 0;
    text-align: center;
    color: var(--author-ink);
    font-family: "Bebas Neue", sans-serif;
    font-size: 25px;
    line-height: 30px;
    letter-spacing: 0.3px;
  }
</style>
</head>
<body>
<main class="canvas">
  <article class="cover">
    <svg class="cover-art" viewBox="0 0 444 644" preserveAspectRatio="none" role="img" aria-label="Sunset sky with a double-exposure silhouette of an athlete flexing both arms, and a small figure with raised arms standing on a hilltop">
      <defs>
        <linearGradient id="sky" x1="0" y1="0" x2="0" y2="1">
          <stop offset="0" stop-color="var(--sky-top)"/>
          <stop offset="0.22" stop-color="var(--sky-upper)"/>
          <stop offset="0.45" stop-color="var(--sky-mid)"/>
          <stop offset="0.68" stop-color="#b8945e"/>
          <stop offset="0.86" stop-color="#7c6048"/>
          <stop offset="1" stop-color="var(--ground)"/>
        </linearGradient>
        <radialGradient id="sun" cx="0.47" cy="0.62" r="0.5" gradientTransform="translate(0.47 0.62) scale(1 0.7) translate(-0.47 -0.62)">
          <stop offset="0" stop-color="var(--sun-core)" stop-opacity="0.95"/>
          <stop offset="0.35" stop-color="var(--sky-glow)" stop-opacity="0.7"/>
          <stop offset="1" stop-color="var(--sky-glow)" stop-opacity="0"/>
        </radialGradient>
        <radialGradient id="hill" cx="1" cy="1" r="0.6">
          <stop offset="0" stop-color="var(--ground)" stop-opacity="1"/>
          <stop offset="0.55" stop-color="var(--ground)" stop-opacity="0.85"/>
          <stop offset="1" stop-color="var(--ground)" stop-opacity="0"/>
        </radialGradient>
        <linearGradient id="base" x1="0" y1="0" x2="0" y2="1">
          <stop offset="0.84" stop-color="var(--ground)" stop-opacity="0"/>
          <stop offset="0.92" stop-color="var(--ground)" stop-opacity="0.9"/>
          <stop offset="1" stop-color="var(--ground)" stop-opacity="1"/>
        </linearGradient>
        <radialGradient id="figure-tone" cx="0.5" cy="0.55" r="0.5">
          <stop offset="0" stop-color="#8a6a50" stop-opacity="0.35"/>
          <stop offset="1" stop-color="#8a6a50" stop-opacity="0"/>
        </radialGradient>
      </defs>
      <rect width="444" height="644" fill="url(#sky)"/>
      <rect width="444" height="644" fill="url(#sun)"/>
      <ellipse cx="210" cy="430" rx="190" ry="150" fill="url(#figure-tone)"/>
      <rect width="444" height="644" fill="url(#hill)"/>
      <rect width="444" height="644" fill="url(#base)"/>
    </svg>
    <h1 class="title">
      <span class="title-light">NURTURING</span>
      <span class="title-bold">VICTORS</span>
    </h1>
    <p class="subtitle">The Foundations of Humble Mentoring for<br>Trainers, Instructors and Players</p>
    <p class="author">Dr. Martin Hollis</p>
  </article>
</main>
</body>
</html>
```